Webpage for a treatment housing for young addicts.

I need a new design and files for my wordpress page. I need it to be more neat and clean. I need it to look professional with a starting page that will work as a navigation. I need like logo and phone number and such up top, a picture under it with one sentence as a slogan and under it 6 boxes to click to come to our different pages. Under it I want news etc.

Target Market(s)

Social services, employees and governements

Coding

Coded - Design and coding required

Font styles to use
Sans Serif

Colors
abd037
3176b5
9d9d9d
aaaaaa
f04a50

Requirements
Must have
• A nice design
Nice to have
• need it to look professional with a starting page that will work as a navigation. I need like logo and phone number and such up top, a picture under it with one sentence as a slogan and under it 6 boxes to click to come to our different pages. Under it I want news etc.
• today www.kolrev.se
• want more like www.tralvik.se or www.bersona.se
Should not have
• To many different colours and a messy design.

```html
<!DOCTYPE html>
<html lang="sv">
<head>
<meta charset="utf-8">
<title>Kolrev – Hem för vård och boende</title>
<link rel="stylesheet" href="https://fonts.googleapis.com/css2?family=Montserrat:wght@400;500;600;700&display=swap">
<style>
:root{
  --green:#8cc63f;
  --green-text:#7ab833;
  --blue:#0d4ea0;
  --footer-blue:#0b57a8;
  --text:#333;
  --white:#fff;
}
*{box-sizing:border-box;margin:0;padding:0}
html,body{width:777px;height:1200px;overflow:hidden;background:var(--white)}
body{position:relative;font-family:"Montserrat",sans-serif;color:var(--text)}
.abs{position:absolute}

.site-header{left:0;top:0;width:777px;height:70px;background:var(--white)}
.brand{left:130px;top:20px;display:flex;align-items:center;gap:7px}
.brand-mark{width:22px;height:22px;background:var(--green)}
.brand-name{font-weight:700;font-size:22px;color:var(--blue);letter-spacing:.5px}
.contact{left:456px;top:15px;font-size:9.5px;letter-spacing:1px;line-height:12.5px;color:#333}
.contact li{list-style:none;display:flex;align-items:center;gap:5px}
.contact svg{width:9px;height:9px;fill:var(--blue)}

.hero{left:0;top:70px;width:777px;height:380px;
  background:linear-gradient(180deg,#3f74b3 0%,#8fb3d6 38%,#e9c7a2 62%,#f39a3a 78%,#1b1410 90%,#0b0908 100%)}
.hero-title{left:0;top:150px;width:777px;text-align:center;color:var(--white);font-weight:700;font-size:22px;letter-spacing:2.6px;line-height:29px}
.nav{left:245px;top:350px;width:288px;display:grid;grid-template-columns:repeat(3,90px);column-gap:9px;row-gap:6px}
.nav a{display:flex;align-items:center;justify-content:center;height:20px;background:var(--green);color:var(--white);font-size:8.5px;font-weight:600;text-decoration:none}

.intro-title,.ideas-title{left:0;width:777px;text-align:center;color:var(--green-text)}
.intro-title{top:466px;font-size:13.5px;font-weight:500;letter-spacing:2.4px}
.intro-text{left:176px;top:498px;width:432px;font-size:8.8px;letter-spacing:1.3px;line-height:16.2px}
.btn{display:flex;align-items:center;justify-content:center;background:var(--blue);color:var(--white);border-radius:12px;font-size:8.5px;font-weight:500;text-decoration:none}
.btn-more{left:353px;top:620px;width:71px;height:22px}

.gallery{left:0;top:673px;width:777px;height:170px;display:flex}
.gallery div{flex:1;height:100%}
.g1{background:linear-gradient(180deg,#e6ecef 0%,#b28c76 40%,#8d3c36 60%,#b3b08d 78%,#8e9a5e 100%)}
.g2{background:linear-gradient(180deg,#dfe6ea 0%,#c9d1d2 30%,#8a2e2e 52%,#6c8a48 72%,#7e9a52 100%)}
.g3{background:linear-gradient(90deg,#d8dfe2 0%,#8e9467 30%,#a55a4a 55%,#8a3a30 100%)}

.ideas-title{top:860px;font-size:13.5px;font-weight:600}
.ideas-text{left:166px;top:883px;width:447px;font-size:8.8px;letter-spacing:1.5px;line-height:16.2px;text-align:justify;text-align-last:left}
.btn-treatment{left:294px;top:1001px;width:190px;height:22px}

.site-footer{left:0;top:1063px;width:777px;height:137px;background:var(--footer-blue);color:var(--white)}
.footer-links{left:130px;top:21px;list-style:none;font-size:9px;letter-spacing:1.6px;line-height:15.6px}
.footer-contact{left:322px;top:21px;font-size:8.8px;letter-spacing:1.3px;line-height:12px}
.footer-contact dt{font-weight:700;letter-spacing:1.8px}
.footer-contact dd{margin-bottom:4px}
.legal{left:462px;top:24px;font-size:8.5px;line-height:15.5px}
.newsletter-title{left:465px;top:76px;font-size:8.5px;font-weight:700}
.newsletter{left:465px;top:95px;display:flex;height:21px}
.newsletter input{width:131px;height:21px;border:0;padding:0 7px;font-family:inherit;font-size:7px;color:#999}
.newsletter button{width:51px;height:21px;border:0;background:#222;color:var(--white);font-family:inherit;font-size:6.5px}
</style>
</head>
<body>

<header class="site-header abs">
  <div class="brand abs"><span class="brand-mark"></span><span class="brand-name">Kolrev</span></div>
  <ul class="contact abs">
    <li><svg viewBox="0 0 10 10"><path d="M1 3 Q1 1 3 1 L7 1 Q9 1 9 3 L7 4 L7 3 L3 3 L3 4 Z M2 5 L8 5 L9 9 L1 9 Z"/></svg>010-4417260</li>
    <li><svg viewBox="0 0 10 10"><circle cx="5" cy="5" r="4.2" fill="none" stroke="#0d4ea0" stroke-width="1.2"/><path d="M5 2.5 V5 H7" stroke="#0d4ea0" stroke-width="1" fill="none"/></svg>Måndag - Fredag 09:00 - 18:00</li>
    <li><svg viewBox="0 0 10 10"><path d="M0 2 H10 V8 H0 Z"/><path d="M0 2 L5 6 L10 2" stroke="#fff" stroke-width=".8" fill="none"/></svg>info@kolrev.se</li>
  </ul>
</header>

<section class="hero abs" role="img" aria-label="Två personer i siluett med armarna i luften mot en solnedgång över skogsklädda kullar"></section>
<h1 class="hero-title abs">Vi skapar Hållbara vägar<br>till en Bättre framtid</h1>
<nav class="nav abs">
  <a href="#">Hem</a><a href="#">Om Kolrev</a><a href="#">Ekbackagården HVB</a>
  <a href="#">Jobba hos oss</a><a href="#">Behandling</a><a href="#">Kontakt</a>
</nav>

<h2 class="intro-title abs">Hem för vård och boende</h2>
<p class="intro-text abs">Kolrev Sverige AB bedriver vård och omsorg riktat mot personer i ålder 14-25 år. Detta görs främst genom Hem för vård och boende (HVB ). Vi är specialister på psykosocial- missbruks- och kriminalitetsproblem. Genom att ständigt vara öppna för nya metoder och väl medvetna om de befint-liga som fungerar utvecklar vi och förbättrar vården. Metoderna anpassas efter individen, vi tror inte att EN tanke eller ETT perspektiv går att applicera på alla.</p>
<a class="btn btn-more abs" href="#">Läs mer</a>

<div class="gallery abs">
  <div class="g1" role="img" aria-label="Vit och röd gård med tegeltak och gräsmatta"></div>
  <div class="g2" role="img" aria-label="Röda trähus med vita knutar på en gräsplan"></div>
  <div class="g3" role="img" aria-label="Tegelbyggnad med grönska längs fasaden"></div>
</div>

<h2 class="ideas-title abs">Våra idéer kring arbetssätt &amp; behandling</h2>
<p class="ideas-text abs">Vi vill genom evidensbaserade metoder, hög kompetens och samlad erfarenhet skapa en terapeutisk behandlingsmiljö. Vi vill att varje individ ska få möjlighet till att förändra och påverka sin egen situation till en bättre och mer välfungerande. Varje person skall bli sedd utifrån sina egna förutsättningar och behov. Sedan ska behandlingen utgå från just dessa förutsättningarna och individuella behov.</p>
<a class="btn btn-treatment abs" href="#">Läs gärna mer om vår behandling</a>

<footer class="site-footer abs">
  <ul class="footer-links abs">
    <li>Hem</li><li>Om Kolrev</li><li>Ekbackagarden HVB</li><li>Jobba hos oss</li><li>Behandling</li><li>Kontakt</li>
  </ul>
  <dl class="footer-contact abs">
    <dt>Telefon</dt><dd>010-4417260</dd>
    <dt>Tidtabell</dt><dd>Måndag - Fredag<br>09:00 - 18:00</dd>
    <dt>E-post</dt><dd>info@kolrev.se</dd>
  </dl>
  <p class="legal abs">Copyrigth 2018 Kolrev AB<br>Personuppgifter – Tillgänglighet – Cookies</p>
  <p class="newsletter-title abs">Prenumerera på vårt nyhetsbrev</p>
  <form class="newsletter abs"><input type="email" placeholder="E-post"><button type="button">SUBSCRIBE</button></form>
</footer>

</body>
</html>
```